Bramblecrest Roofing Co. business card design

I am a Roofing contractor in Texas. The name of my company is Bramblecrest Roofing Co. I also offer a few other services (Christmas light installation, gutters, fencing, pressure washing). However my main gig is roofing. Storm restoration and knowledge of the insurance claim process is my specialty.

My colors are black, red and white. I’d like something pretty simple and clean. Modern looking but with a splash of this red tartan pattern.

I have another version of my logo being edited at the moment where the little top part of the F in roofing that’s currently tartan will be changed to just solid red to make it more visible. So if that’s something you can change in your mock up great. But I can provide the full version once the contest is complete

Target Market(s)

Homeowners

Industry/Entity Type

Roofing

Contact Information for Business Card

Darren Pike. 682-555-0193. www.bramblecrest roofing.example Darren@bramblecrestroofing.example

Colors
EB3D1F
EC4F4E
F09395
F8D3D4
FCEDEE

Requirements
Nice to have
• Maybe instead of a business address. I could say serving all DFW Texas or something like that. And maybe add a line somewhere saying deductible assistance? Just a thought

```html
<!DOCTYPE html>
<html lang="en">
<head>
<meta charset="utf-8">
<title>Bramblecrest Roofing Co. – Business Card</title>
<link rel="stylesheet" href="https://fonts.googleapis.com/css2?family=Montserrat:wght@300;400;700;800&display=swap">
<style>
  :root {
    --page-bg: #2b2b2b;
    --card-bg: #1c1c1c;
    --brand-red: #e0161f;
    --brand-red-dark: #a90f16;
    --white: #ffffff;
    --muted: #d9d9d9;
  }
  * { box-sizing: border-box; margin: 0; padding: 0; }
  html, body {
    width: 1200px; height: 900px; overflow: hidden;
    background: var(--page-bg);
    font-family: "Montserrat", sans-serif;
  }
  .canvas {
    position: relative; width: 1200px; height: 900px;
    display: flex; flex-direction: column; align-items: center; justify-content: center; gap: 60px;
  }
  .card {
    width: 595px; height: 340px;
    background: var(--card-bg);
    border-radius: 4px;
    box-shadow: 0 14px 30px rgba(0,0,0,.45);
    position: relative; overflow: hidden;
  }

  /* Brand lockup */
  .brand { display: flex; flex-direction: column; align-items: center; }
  .brand-mark {
    border-radius: 50%;
    background: radial-gradient(circle at 50% 45%, var(--brand-red) 0%, var(--brand-red-dark) 100%);
    border: 4px solid var(--white);
  }
  .brand-name {
    color: var(--white);
    font-weight: 800;
    text-transform: uppercase;
    text-align: center;
    line-height: 1.05;
    letter-spacing: 1px;
  }

  /* Front */
  .card-front { display: flex; align-items: center; justify-content: center; }
  .card-front .brand-mark { width: 130px; height: 130px; margin-bottom: 16px; }
  .card-front .brand-name { font-size: 30px; }

  /* Back */
  .card-back { display: flex; align-items: center; padding: 0 40px 0 34px; }
  .card-back .brand { width: 235px; }
  .card-back .brand-mark { width: 92px; height: 92px; margin-bottom: 12px; }
  .card-back .brand-name { font-size: 19px; }
  .divider {
    width: 2px; height: 150px; background: var(--brand-red);
    margin: 0 30px 0 22px; flex-shrink: 0;
  }
  .contact { color: var(--white); }
  .contact-name { color: var(--brand-red); font-weight: 700; font-size: 22px; }
  .contact-role { font-weight: 300; font-size: 12px; margin-bottom: 14px; }
  .contact-address { font-weight: 400; font-size: 12px; line-height: 1.35; margin-bottom: 12px; }
  .contact-list { list-style: none; font-size: 11.5px; line-height: 1.55; }
  .contact-list li { display: flex; align-items: center; gap: 8px; }
  .contact-list svg { width: 11px; height: 11px; fill: var(--brand-red); flex-shrink: 0; }
</style>
</head>
<body>
<main class="canvas">

  <section class="card card-front" aria-label="Card front">
    <div class="brand">
      <div class="brand-mark" role="img" aria-label="Brand emblem: red circle with white ring"></div>
      <p class="brand-name">Bramblecrest<br>Roofing Co.</p>
    </div>
  </section>

  <section class="card card-back" aria-label="Card back">
    <div class="brand">
      <div class="brand-mark" role="img" aria-label="Brand emblem: red circle with white ring"></div>
      <p class="brand-name">Bramblecrest<br>Roofing Co.</p>
    </div>
    <span class="divider"></span>
    <div class="contact">
      <p class="contact-name">Darren Pike</p>
      <p class="contact-role">Owner</p>
      <p class="contact-address">1480 Cedar Hollow Rd<br>Fort Worth, TX 76102</p>
      <ul class="contact-list">
        <li>
          <svg viewBox="0 0 24 24" aria-hidden="true"><path d="M6.6 10.8a15.1 15.1 0 0 0 6.6 6.6l2.2-2.2c.3-.3.7-.4 1-.2 1.1.4 2.3.6 3.6.6.6 0 1 .4 1 1V20c0 .6-.4 1-1 1A17 17 0 0 1 3 4c0-.6.4-1 1-1h3.5c.6 0 1 .4 1 1 0 1.2.2 2.4.6 3.6.1.3 0 .7-.2 1z"/></svg>
          682-555-0193
        </li>
        <li>
          <svg viewBox="0 0 24 24" aria-hidden="true"><path d="M2 5h20v14H2zm2 2v.5l8 5 8-5V7l-8 5z"/></svg>
          info@bramblecrestroofing.example
        </li>
        <li>
          <svg viewBox="0 0 24 24" aria-hidden="true"><path d="M12 2a10 10 0 1 0 0 20 10 10 0 0 0 0-20zm6.9 6h-2.9a15.6 15.6 0 0 0-1.4-3.6A8 8 0 0 1 18.9 8zM12 4c.8 1.2 1.5 2.5 1.9 4h-3.8c.4-1.5 1.1-2.8 1.9-4zM4.3 14a8 8 0 0 1 0-4h3.4a16 16 0 0 0 0 4zm.8 2h2.9c.3 1.3.8 2.5 1.4 3.6A8 8 0 0 1 5.1 16zM8 8H5.1a8 8 0 0 1 4.3-3.6C8.8 5.5 8.3 6.7 8 8zm4 12c-.8-1.2-1.5-2.5-1.9-4h3.8c-.4 1.5-1.1 2.8-1.9 4zm2.3-6H9.7a14.7 14.7 0 0 1 0-4h4.6a14.7 14.7 0 0 1 0 4zm.3 5.6c.6-1.1 1.1-2.3 1.4-3.6h2.9a8 8 0 0 1-4.3 3.6zm1.7-5.6a16 16 0 0 0 0-4h3.4a8 8 0 0 1 0 4z"/></svg>
          www.bramblecrestroofing.example
        </li>
      </ul>
    </div>
  </section>

</main>
</body>
</html>
```